Business cards and logo for kitchen and bath remodeling company

We want an elegant card but that calls attention something unique and when people see it they remember us. A log that we can use for our own. We are a kitchen and bathroom remodeling company. We are 3 partners staring the company we are located in seattle washington usa. We try to give the best experience and luxury look in our projects and we are looking to show that in our cards. I added a sample of a card I really like. I like the black and gold look but gray blue or green in a metallic look would look nice. I'm open to any color.

Target Market(s)

Home owners.

Industry/Entity Type

Construction

Contact Information for Business Card

Larchmont and Vey builders

Colors

Designer to choose colors to be used in the design.

Requirements
Must have
• Make a Logo
• Logo to be unique
• Name of company larchmont and vey builders
Nice to have
• Have a good color scheme
• Front design to connect with back of card

```html
<!DOCTYPE html>
<html lang="en">
<head>
<meta charset="utf-8">
<title>Larchmont &amp; Vey — Business Card</title>
<link href="https://fonts.googleapis.com/css2?family=Montserrat:wght@400;500;600;700&display=swap" rel="stylesheet">
<style>
  :root {
    --page: #1b1b1c;
    --card: #2a2a2b;
    --gold: #b8903a;
    --gold-soft: #a88a4e;
    --shadow: rgba(0,0,0,0.55);
  }
  * { box-sizing: border-box; margin: 0; padding: 0; }
  html, body {
    width: 1200px; height: 912px; overflow: hidden;
    background: var(--page);
    font-family: "Montserrat", sans-serif;
  }
  .sheet {
    width: 1200px; height: 912px;
    display: flex; flex-direction: column;
    align-items: center; justify-content: center; gap: 48px;
  }
  .card {
    width: 620px; height: 354px;
    background: var(--card);
    box-shadow: 0 18px 40px var(--shadow);
    position: relative;
  }

  /* Back side */
  .card-back {
    display: flex; align-items: center;
    padding: 0 56px;
  }
  .back-brand {
    width: 190px;
    display: flex; align-items: center; gap: 10px;
    color: var(--gold);
    font-weight: 600; font-size: 17px; letter-spacing: 1px;
    line-height: 1.25;
  }
  .brand-square {
    width: 12px; height: 12px; flex: none;
    border: 2px solid var(--gold);
  }
  .divider {
    width: 2px; height: 112px;
    background: var(--gold-soft);
    margin: 0 30px 0 24px;
  }
  .contact { color: var(--gold-soft); }
  .contact-name {
    font-weight: 600; font-size: 18px; letter-spacing: 0.5px;
    color: var(--gold);
    margin-bottom: 12px;
  }
  .contact-line {
    display: flex; align-items: center; gap: 10px;
    font-size: 14px; letter-spacing: 0.6px;
    margin-top: 6px;
  }
  .contact-icon {
    width: 14px; height: 14px; flex: none;
  }

  /* Front side */
  .card-front {
    display: flex; flex-direction: column;
    align-items: center; justify-content: center;
  }
  .front-square {
    width: 22px; height: 22px;
    border: 2px solid var(--gold);
    margin-bottom: 22px;
  }
  .wordmark {
    color: var(--gold);
    font-weight: 700; font-size: 42px; letter-spacing: 6px;
  }
  .tagline {
    color: var(--gold);
    font-weight: 500; font-size: 13px; letter-spacing: 1.4px;
    margin-top: 10px;
  }
</style>
</head>
<body>
<main class="sheet">
  <section class="card card-back" aria-label="Card back">
    <div class="back-brand"><span class="brand-square"></span><span>LARCHMONT &amp; VEY</span></div>
    <div class="divider"></div>
    <div class="contact">
      <p class="contact-name">Marisol Fenwick</p>
      <p class="contact-line">
        <svg class="contact-icon" viewBox="0 0 14 14"><circle cx="7" cy="7" r="7" fill="#a88a4e"/><path d="M4.6 3.8l1.2 1.3-.6.9c.5 1 1.2 1.7 2.2 2.2l.9-.6 1.3 1.2-.7 1.2c-2.6-.3-4.7-2.4-5-5z" fill="#2a2a2b"/></svg>
        Cell: 206 555 0147
      </p>
      <p class="contact-line">
        <svg class="contact-icon" viewBox="0 0 14 14"><circle cx="7" cy="7" r="7" fill="#a88a4e"/><rect x="3.5" y="4.5" width="7" height="5" fill="none" stroke="#2a2a2b" stroke-width="1"/><path d="M3.5 4.8L7 7.4l3.5-2.6" fill="none" stroke="#2a2a2b" stroke-width="1"/></svg>
        E-mail: hello@larchvey.com
      </p>
      <p class="contact-line">
        <svg class="contact-icon" viewBox="0 0 14 14"><circle cx="7" cy="7" r="7" fill="#a88a4e"/><circle cx="7" cy="7" r="3.6" fill="none" stroke="#2a2a2b" stroke-width="1"/><path d="M3.4 7h7.2M7 3.4c-1.4 1.8-1.4 5.4 0 7.2M7 3.4c1.4 1.8 1.4 5.4 0 7.2" fill="none" stroke="#2a2a2b" stroke-width="0.8"/></svg>
        Web: www.larchvey.com
      </p>
    </div>
  </section>

  <section class="card card-front" aria-label="Card front">
    <span class="front-square"></span>
    <h1 class="wordmark">LARCHMONT &amp; VEY</h1>
    <p class="tagline">KITCHEN AND BATH PROFESSIONALS</p>
  </section>
</main>
</body>
</html>
```